FLUSH FAIRY the solution to twinkle the smell away...because everyone poops

I need a label for my handmade poop spray. Flush fairy is an organic blend of essential oils that eliminates the odor when you poop. Directions must be on the back of the label : shake well before each use. Spray on the toilet water surface 4-6 times to cover the water before you go. Poop as usual and flush. Safe for all pipes and sewer systems. To order visit my Wovi shop enter flush fairy

Font styles to use
Decorative

Requirements
Must have
• Directions on how to use
Nice to have
• Elegant design label. Product is meant to be kept in the bathroom

```html
<!DOCTYPE html>
<html lang="en">
<head>
<meta charset="utf-8">
<title>Flush Fairy – Label</title>
<link rel="stylesheet" href="https://fonts.googleapis.com/css2?family=Crimson+Text:wght@700&display=swap">
<style>
  :root {
    --page: #ffffff;
    --red: #dc2410;
    --red-deep: #d2160c;
    --red-soft: #e05050;
    --orange: #ff6a06;
    --orange-light: #ff8a2a;
    --ink: #ffffff;
  }
  * { margin: 0; padding: 0; box-sizing: border-box; }
  html, body {
    width: 1200px; height: 542px; overflow: hidden;
    background: var(--page);
  }
  .canvas { position: relative; width: 1200px; height: 542px; }
  .label {
    position: absolute; left: 59px; top: 144px;
    width: 1089px; height: 256px; overflow: hidden;
    background: var(--red);
  }
  .label__art { position: absolute; inset: 0; }
  .copy {
    position: absolute;
    font-family: "Crimson Text", Georgia, serif;
    font-weight: 700;
    color: var(--ink);
  }
  .copy--intro {
    left: 273px; top: 80px; width: 273px;
    text-align: center; font-size: 12.5px; line-height: 17px;
  }
  .copy--directions {
    left: 562px; top: 28px; width: 230px;
    font-size: 12px; line-height: 17px;
  }
  .copy--back {
    right: 14px; top: 166px; width: 200px;
    text-align: right; font-size: 10px; line-height: 13px;
  }
  .brand {
    position: absolute; left: 30px; top: 98px; width: 215px;
    display: flex; align-items: center; justify-content: center; gap: 8px;
    font-family: "Crimson Text", Georgia, serif;
    font-weight: 700; font-size: 38px; line-height: 1;
    color: var(--ink);
  }
  .brand__dot {
    width: 14px; height: 14px; border-radius: 50%;
    background: var(--ink); flex: none;
  }
  .toilet-illustration {
    position: absolute; left: 661px; top: 92px;
    width: 118px; height: 134px;
    background: linear-gradient(180deg, #ffffff, #fbe3dc);
    border-radius: 10px;
  }
</style>
</head>
<body>
<main class="canvas">
  <section class="label">
    <svg class="label__art" viewBox="0 0 1089 256" preserveAspectRatio="none" aria-hidden="true">
      <!-- panels -->
      <rect x="0" y="0" width="273" height="256" fill="var(--red)"/>
      <rect x="273" y="0" width="273" height="256" fill="var(--red)"/>
      <rect x="546" y="0" width="272" height="256" fill="var(--red)"/>
      <rect x="818" y="0" width="271" height="256" fill="var(--red-deep)"/>
      <!-- upper orange field -->
      <path d="M546,0 L1089,0 L1089,240 C1040,150 930,80 780,70 C690,64 610,66 546,70 Z" fill="var(--orange)"/>
      <!-- main swoosh -->
      <path d="M0,185 C120,150 300,60 546,0 L600,0 C450,40 300,110 160,160 C100,180 40,200 0,215 Z" fill="var(--orange-light)"/>
      <!-- lower stripe -->
      <path d="M546,130 C680,70 880,60 1000,120 C1040,140 1070,170 1089,210 L1089,230 C1060,180 1020,150 980,135 C870,90 700,100 546,145 Z" fill="var(--orange)"/>
      <!-- soft overlay panel -->
      <rect x="273" y="0" width="273" height="256" fill="#ffffff" opacity="0.22"/>
    </svg>

    <div class="brand"><span class="brand__dot"></span>Flush Fairy</div>

    <p class="copy copy--intro">Flush Fairy Is Delicate<br>BlendOf Organic Essential<br>Oils That TrapIndesrable<br>Smell And Odors Sealing The<br>Aromas Allowing You To Forget<br>About Courtesy Flushing</p>

    <p class="copy copy--directions">Shake 4-6 Times In Toilet BowlIn Corner<br>The Water Surface Before You Poop.<br>This Will AbsorbThe Odors.<br>Flush And You're Done It.</p>

    <div class="toilet-illustration" role="img" aria-label="Toilet illustration with spray-here markers"></div>

    <p class="copy copy--back">Flush Fairy Is Delicate<br>BlendOf Organic Essential<br>Oils That TrapIndesrable<br>Smell And Odors Sealing The<br>Aromas Allowing You To Forget<br>About Courtesy Flushing</p>
  </section>
</main>
</body>
</html>
```